" Clínica médica que atua nas diversas especialidades e realiza atendimentos particulares a preços acessíveis, podendo futuramente atender planos de saúde. "

```html
<!DOCTYPE html>
<html lang="pt-BR">
<head>
<meta charset="utf-8">
<title>VitaClin — Clínica Médica</title>
<link href="https://fonts.googleapis.com/css2?family=Roboto:wght@400;500;700&display=swap" rel="stylesheet">
<style>
  :root {
    --page-bg: #e4e4e4;
    --green-dark: #1d4a36;
    --green-header: #235a41;
    --green-text: #1f5a3f;
    --green-soft: #7fb79a;
    --white: #ffffff;
    --nav-rule: #d9e3dd;
    --section-bg: #f1f2f1;
  }
  * { box-sizing: border-box; margin: 0; padding: 0; }
  html, body {
    width: 1200px; height: 1200px; overflow: hidden;
    background: var(--page-bg);
    font-family: "Roboto", sans-serif;
  }
  .site {
    position: absolute; left: 330px; top: 28px;
    width: 540px; height: 1144px;
    background: var(--white);
    display: flex; flex-direction: column;
    overflow: hidden;
  }
  .site-header {
    height: 118px; display: flex;
    background: var(--green-header);
  }
  .brand {
    width: 50%; display: flex; align-items: center; justify-content: center; gap: 14px;
    background: var(--green-dark);
    border-right: 3px solid var(--white);
  }
  .brand-dot { width: 22px; height: 22px; border-radius: 50%; background: var(--green-soft); }
  .brand-text { display: flex; flex-direction: column; color: var(--white); }
  .brand-name { font-size: 40px; font-weight: 500; line-height: 1; }
  .brand-tag { font-size: 11px; font-weight: 500; letter-spacing: 2px; text-transform: uppercase; margin-top: 4px; }
  .header-cta {
    width: 50%; display: flex; align-items: center; justify-content: center;
    color: var(--white); font-size: 30px; font-weight: 500; text-align: center; line-height: 1.2;
  }
  .main-nav {
    height: 160px; display: grid; grid-template-columns: 1fr 1fr;
    align-items: center; padding: 10px 24px;
    border-bottom: 1px solid var(--nav-rule);
  }
  .main-nav a {
    color: var(--green-text); text-decoration: none; text-align: center;
    font-size: 26px; line-height: 1.15;
  }
  .hero {
    position: relative; height: 680px; overflow: hidden;
  }
  .hero-photo {
    position: absolute; inset: 0;
    background:
      radial-gradient(ellipse 40% 35% at 55% 35%, #e6d3c4 0%, rgba(230,211,196,0) 70%),
      radial-gradient(ellipse 45% 40% at 55% 85%, #f4f6f5 0%, rgba(244,246,245,0) 75%),
      linear-gradient(120deg, #3f9a6c 0%, #8fc9a6 40%, #cfe3d6 70%, #a9cdb7 100%);
  }
  .hero-shade {
    position: absolute; left: 0; right: 0; bottom: 0; height: 320px;
    background: linear-gradient(to top, rgba(20,60,40,0.55), rgba(20,60,40,0));
  }
  .hero-content {
    position: absolute; left: 36px; right: 24px; top: 430px; color: var(--white);
  }
  .hero-title { font-size: 31px; font-weight: 500; line-height: 1.1; }
  .hero-sub { font-size: 17px; margin-top: 6px; }
  .hero-actions { display: flex; gap: 22px; margin-top: 30px; }
  .btn {
    font-size: 14px; padding: 16px 14px; text-decoration: none;
  }
  .btn-primary { background: var(--green-dark); color: var(--white); }
  .btn-secondary { background: var(--white); color: var(--green-text); }
  .promo {
    flex: 1; display: flex; background: var(--section-bg); position: relative;
  }
  .promo-title {
    padding: 18px 0 0 54px; color: var(--green-dark);
    font-size: 34px; font-weight: 700; line-height: 1.1; width: 56%;
  }
  .promo-photo {
    position: absolute; right: 0; top: 50px; width: 230px; bottom: 0;
    background: linear-gradient(160deg, #5a3f33 0%, #c9a18c 45%, #efe6e0 100%);
  }
</style>
</head>
<body>
  <div class="site">
    <header class="site-header">
      <div class="brand">
        <span class="brand-dot"></span>
        <div class="brand-text">
          <span class="brand-name">VitaClin</span>
          <span class="brand-tag">Clínica Médica</span>
        </div>
      </div>
      <div class="header-cta">Agendamento e<br>Resultados</div>
    </header>

    <nav class="main-nav">
      <a href="#">Quem Somos</a>
      <a href="#">Exames</a>
      <a href="#">Consultas<br>e Tratamentos</a>
      <a href="#">Fale Conosco</a>
    </nav>

    <section class="hero">
      <div class="hero-photo" role="img" aria-label="Fotografia de médico sorridente de jaleco branco com estetoscópio em consultório"></div>
      <div class="hero-shade"></div>
      <div class="hero-content">
        <h1 class="hero-title">Faça agora o seu agendamento.</h1>
        <p class="hero-sub">Clique em uma das opções abaixo e escolha seu serviço.</p>
        <div class="hero-actions">
          <a class="btn btn-primary" href="#">Agendar uma consulta</a>
          <a class="btn btn-secondary" href="#">Agendar um exame</a>
        </div>
      </div>
    </section>

    <section class="promo">
      <h2 class="promo-title">Resultados rápidos. Marcação de Exames</h2>
      <div class="promo-photo" role="img" aria-label="Fotografia de mãe e filha sorrindo juntas"></div>
    </section>
  </div>
</body>
</html>
```